Velra Orchards Business Cards

design business cards for our new business should match my Copperline Quotes business cards

Contact Information for Business Card

2817 N 48th W Ave
Tulsa, OK 74146

Requirements
Must have
• should match logo colors

```html
<!DOCTYPE html>
<html lang="en">
<head>
<meta charset="utf-8">
<title>Velra Orchards – Business Card Design</title>
<link rel="stylesheet" href="https://fonts.googleapis.com/css2?family=Montserrat:ital,wght@0,300;0,500;0,600;0,700;0,800;1,700&family=Orbitron:wght@700&display=swap">
<style>
  :root{
    --leaf-green:#7dc242;
    --teal:#1aa9ae;
    --navy:#1f2b38;
    --white:#ffffff;
    --board-grey:#a9a9a9;
    --strip-grey:#5b5b5b;
    --ink:#1c1c1c;
  }
  *{margin:0;padding:0;box-sizing:border-box}
  html,body{width:1200px;height:1200px;overflow:hidden}
  body{
    position:relative;
    background:radial-gradient(circle at 60% 45%, #c4c4c4 0%, var(--board-grey) 75%);
    font-family:"Montserrat",sans-serif;
  }
  .side-label{
    position:absolute;left:0;top:0;width:126px;height:1200px;
    background:var(--strip-grey);
  }
  .side-label span{
    position:absolute;left:63px;top:600px;
    transform:translate(-50%,-50%) rotate(-90deg);
    white-space:nowrap;color:var(--white);
    font-size:56px;letter-spacing:2px;
  }
  .side-label b{font-weight:800}
  .side-label i{font-style:normal;font-weight:300}

  .card{position:absolute;left:222px;width:882px;height:524px;overflow:hidden}
  .card svg.shapes{position:absolute;inset:0}
  .card--front{top:46px}
  .card--back{top:624px;background:var(--white)}

  .pattern-area{
    position:absolute;left:50px;top:118px;width:790px;height:330px;
    background:linear-gradient(90deg,rgba(255,255,255,.10),rgba(255,255,255,.16),rgba(255,255,255,.10));
  }
  .wordmark{
    position:absolute;font-weight:700;text-transform:uppercase;line-height:1;
  }
  .wordmark--front{left:0;right:0;top:168px;text-align:center;color:var(--white)}
  .wordmark--front .line1{display:block;font-size:150px;letter-spacing:6px}
  .wordmark--front .line2{display:block;font-size:56px;letter-spacing:20px;margin-top:18px}
  .wordmark--back{left:28px;width:340px;top:178px;text-align:center;color:var(--leaf-green)}
  .wordmark--back .line1{display:block;font-size:84px;letter-spacing:3px}
  .wordmark--back .line2{display:block;font-size:33px;letter-spacing:9px;margin-top:14px}

  .web{
    position:absolute;left:62px;font-weight:700;font-size:17px;letter-spacing:.5px;
  }
  .card--front .web{top:484px;color:var(--leaf-green)}
  .card--back .web{top:491px;color:var(--white)}

  .person{position:absolute;left:457px;top:158px;width:360px}
  .person__name{
    font-family:"Orbitron",sans-serif;font-weight:700;font-size:29px;letter-spacing:1.5px;
    padding-bottom:2px;border-bottom:2px solid var(--teal);display:inline-block;width:354px;
  }
  .person__name .first{color:var(--leaf-green)}
  .person__name .last{color:var(--teal)}
  .person__role{font-weight:700;font-style:italic;font-size:19px;color:var(--ink);margin-top:8px}

  .contact{position:absolute;left:456px;top:250px;list-style:none}
  .contact li{display:flex;align-items:flex-start;font-weight:500;font-size:17px;color:var(--ink);line-height:22px;margin-bottom:20px}
  .contact svg{width:26px;height:26px;margin-right:16px;flex:none;margin-top:-2px}
</style>
</head>
<body>

<div class="side-label"><span><b>BUSINESS CARD</b> <i>DESIGN</i></span></div>

<!-- Front -->
<section class="card card--front">
  <svg class="shapes" viewBox="0 0 882 524" width="882" height="524">
    <defs>
      <linearGradient id="frontFade" x1="0" x2="1" y1="0" y2="0">
        <stop offset="0" stop-color="#7dc242"/>
        <stop offset=".45" stop-color="#6cbf55"/>
        <stop offset="1" stop-color="#1aa9ae"/>
      </linearGradient>
    </defs>
    <rect width="882" height="524" fill="url(#frontFade)"/>
    <polygon points="426,0 882,0 882,41 462,41" fill="#ffffff"/>
    <polygon points="0,480 408,480 456,524 0,524" fill="#ffffff"/>
  </svg>
  <div class="pattern-area" role="img" aria-label="Faint repeating brand pattern across the card face"></div>
  <div class="wordmark wordmark--front"><span class="line1">Velra</span><span class="line2">Orchards</span></div>
  <div class="web">WWW.VELRAORCHARDS.COM</div>
</section>

<!-- Back -->
<section class="card card--back">
  <svg class="shapes" viewBox="0 0 882 524" width="882" height="524">
    <rect x="0" y="0" width="470" height="20" fill="#7dc242"/>
    <polygon points="462,0 882,0 882,42 420,42" fill="#1aa9ae"/>
    <polygon points="0,484 432,484 474,524 0,524" fill="#7dc242"/>
    <polygon points="450,503 882,503 882,524 472,524" fill="#1aa9ae"/>
  </svg>

  <div class="wordmark wordmark--back"><span class="line1">Velra</span><span class="line2">Orchards</span></div>

  <div class="person">
    <div class="person__name"><span class="first">DARA</span>&nbsp;&nbsp;<span class="last">QUILL</span></div>
    <div class="person__role">President</div>
  </div>

  <ul class="contact">
    <li>
      <svg viewBox="0 0 26 26"><circle cx="13" cy="13" r="11.5" fill="none" stroke="#1f2b38" stroke-width="1.6"/><path d="M9 7.5c.6-.4 1.3-.3 1.7.3l1.2 1.9c.3.5.2 1.1-.2 1.4l-.9.7c.6 1.4 1.7 2.6 3.2 3.3l.7-.9c.4-.4 1-.5 1.4-.2l1.9 1.2c.6.4.7 1.2.3 1.7l-.7.9c-.6.7-1.6.9-2.5.5-3-1.3-5.3-3.6-6.6-6.6-.4-.9-.2-1.9.5-2.5z" fill="#7dc242"/></svg>
      713-555-0142
    </li>
    <li>
      <svg viewBox="0 0 26 26"><circle cx="13" cy="13" r="11.5" fill="none" stroke="#1f2b38" stroke-width="1.6"/><rect x="7" y="9" width="12" height="8.5" rx="1" fill="none" stroke="#7dc242" stroke-width="1.6"/><path d="M7.5 9.6 13 14l5.5-4.4" fill="none" stroke="#7dc242" stroke-width="1.4"/></svg>
      DQuill@velraorchards.com
    </li>
    <li>
      <svg viewBox="0 0 26 26"><circle cx="13" cy="13" r="11.5" fill="none" stroke="#1f2b38" stroke-width="1.6"/><path d="M13 5.5a4.6 4.6 0 0 0-4.6 4.6c0 3.4 4.6 9 4.6 9s4.6-5.6 4.6-9A4.6 4.6 0 0 0 13 5.5z" fill="#7dc242"/><circle cx="13" cy="10.2" r="1.7" fill="#ffffff"/></svg>
      <span>2817 N 48th W Ave<br>Tulsa, OK 74146</span>
    </li>
  </ul>

  <div class="web">WWW.VELRAORCHARDS.COM</div>
</section>

</body>
</html>
```